Dental Practice Billboard Design

We are a newer dental practice in need of a simple but appealing billboard for our growing dental practice to attract new patients. The practice is owned by husband and wife dentists and is family friendly in a small town in Kentucky. We try to be very friendly and caring to our patients. Would prefer a blue background for the billboard and our tooth logo to be prominent. We are partial to the Patua One font used in the image below but please feel free to tweak it as you deem necessary. The shape of the uppercase D and lowercase g are why we like that font, so fonts with a similarly shaped “D” and “g” would work as well. Please include our phone number (606) 847-3962. Please see our website Harlowfamilydentistry.com for more info on the practice if needed. Thank you! Looking forward to seeing your creation.
Updates

The dimensions will be 12ft x 24ft (3.6576m x 7.3152m). Apologies for not including this in the original prompt. Thank you all for your submissions.

Industry/Entity Type

Dental

Font styles to use
Other font styles liked:
• Patua One

Colors
0054AA
0677BA
7BADD7
CADEEF
E8F1F8
0094D4
00A9DD
6FCCEA
C7EBF8
E9F6FB
00AB8E
00BBA5
67D7C9
C6EFE9
E9F9F6
59FF00
82FF00
B8FF75
E3FFCB
F4FFEA

Requirements
Must have
• Phone number, website, Logo, Practice name “Harlow Family Dentistry”
Should not have
• A tagline or slogan

```html
<!DOCTYPE html>
<html lang="en">
<head>
<meta charset="utf-8">
<title>Harlow Family Dentistry – Billboard</title>
<link href="https://fonts.googleapis.com/css2?family=Patua+One&family=Fira+Sans+Condensed:wght@600&display=swap" rel="stylesheet">
<style>
  :root{
    --page:#ffffff;
    --navy-top:#2358a8;
    --navy-bottom:#1b3266;
    --navy-text:#172a5a;
    --green:#33b249;
    --white:#ffffff;
    --photo-warm:#b9977a;
    --photo-brick:#9a5a43;
  }
  html,body{margin:0;padding:0;overflow:hidden;}
  body{width:1200px;height:1062px;background:var(--page);position:relative;}
  .billboard{
    position:absolute;left:40px;top:368px;width:1120px;height:326px;
    background:linear-gradient(180deg,var(--navy-top) 0%,var(--navy-bottom) 100%);
    overflow:hidden;box-shadow:0 4px 14px rgba(0,0,0,.25);
  }
  .billboard__glow{
    position:absolute;left:200px;top:-260px;width:420px;height:300px;border-radius:50%;
    background:rgba(60,120,200,.35);
  }
  .brand{position:absolute;left:0;top:0;}
  .brand__dot{
    position:absolute;left:58px;top:82px;width:96px;height:96px;border-radius:50%;
    background:var(--green);
  }
  .brand__name{
    position:absolute;left:201px;top:52px;margin:0;color:var(--white);
    font-family:"Patua One",serif;font-weight:400;white-space:nowrap;
  }
  .brand__name .line1{display:block;font-size:88px;line-height:88px;}
  .brand__name .line2{display:block;font-size:40px;line-height:44px;margin-left:-10px;}
  .qualities{
    position:absolute;left:556px;top:0;width:376px;height:198px;background:var(--white);
    border-bottom-left-radius:18px;
  }
  .qualities ul{list-style:none;margin:0;padding:22px 0 0 26px;}
  .qualities li{
    font-family:"Patua One",serif;font-size:38px;line-height:51px;color:var(--navy-text);
    display:flex;align-items:center;
  }
  .qualities li::before{
    content:"";width:17px;height:17px;border-radius:50%;background:var(--green);
    margin-right:14px;
  }
  .green-band{position:absolute;right:0;top:0;width:187px;height:326px;background:var(--green);}
  .photo{position:absolute;left:788px;top:28px;width:332px;height:290px;}
  .contact{
    position:absolute;left:28px;top:252px;display:flex;align-items:center;
  }
  .contact__phone{
    font-family:"Fira Sans Condensed",sans-serif;font-weight:600;font-size:48px;color:var(--white);
    margin-left:8px;letter-spacing:-.5px;
  }
  .contact__icon{width:40px;height:40px;}
  .contact__web{
    position:absolute;left:397px;top:254px;width:388px;height:38px;border-radius:6px;
    background:var(--green);color:var(--navy-text);
    font-family:"Patua One",serif;font-size:21px;line-height:38px;text-align:center;
  }
</style>
</head>
<body>
  <section class="billboard">
    <div class="billboard__glow"></div>

    <div class="brand">
      <span class="brand__dot"></span>
      <h1 class="brand__name"><span class="line1">Harlow</span><span class="line2">Family Dentistry</span></h1>
    </div>

    <div class="green-band"></div>

    <div class="qualities">
      <ul>
        <li>EXPERIENCED</li>
        <li>FRIENDLY</li>
        <li>CARING</li>
      </ul>
    </div>

    <svg class="photo" viewBox="0 0 332 290" role="img" aria-label="Photo of the two dentists in white coats smiling in front of a brick building">
      <defs>
        <linearGradient id="photoTone" x1="0" y1="0" x2="1" y2="1">
          <stop offset="0" stop-color="#d8c6b0"/>
          <stop offset=".55" stop-color="#b9977a"/>
          <stop offset="1" stop-color="#9a5a43"/>
        </linearGradient>
      </defs>
      <path d="M40 60 C70 30 110 42 150 22 C200 -2 270 0 305 40 C335 80 325 170 300 220 C275 268 220 282 165 285 C110 288 60 270 35 225 C10 180 12 100 40 60 Z"
            fill="url(#photoTone)" stroke="var(--navy-bottom)" stroke-width="4"/>
    </svg>

    <div class="contact">
      <svg class="contact__icon" viewBox="0 0 40 40" aria-hidden="true">
        <path d="M10 4 L16 4 L19 12 L15 15 C17 21 20 24 25 26 L28 22 L36 25 L36 31 C36 34 34 36 31 36 C16 35 5 24 4 9 C4 6 6 4 10 4 Z" fill="var(--green)"/>
        <path d="M22 18 L33 7 M26 7 L33 7 L33 14" fill="none" stroke="var(--green)" stroke-width="3.5" stroke-linecap="round" stroke-linejoin="round"/>
      </svg>
      <span class="contact__phone">(606) 847-3962</span>
    </div>

    <div class="contact__web">www.harlowfamilydentistry.com</div>
  </section>
</body>
</html>
```